General Contractors need a new Crisp updated Card Design

We need a new business card design for our company of 25 years based in Toronto call Holvaster Building Inc. : Our goal is to be the leading commercial contractors in Toronto by providing exceptional value to our clients. We work very hard to deliver professional, quality, service in conjunction with consistent price competitiveness to all of our clients on every single project.

Target Market(s)

Design & Build Clients

Industry/Entity Type

Construction Company

Contact Information for Business Card

Address:
18 North Tamlin Glen Road, Unit 57, Marbrook Vale, ON, K7T 2R9
Office: 905-218-5937

Holvasters Logo
Employee Job Description
Employee Cell Phone #
Employee Email
www.holvaster-example.com

Colors

Designer to choose colors to be used in the design.

Requirements
Must have
• Quote Company Saying:
• "Professional. Quality. Service."
Nice to have
• New Crisp up to date look. simple & fresh ( Not to Busy)
Should not have
• NO BLUE PRINTS ON THE BUSINESS CARDS

```html
<!DOCTYPE html>
<html lang="en">
<head>
<meta charset="utf-8">
<title>Holvaster Building Inc. — Business Card</title>
<link rel="stylesheet" href="https://fonts.googleapis.com/css2?family=Exo+2:wght@400;500;600&display=swap">
<style>
  :root {
    --backdrop: #03786e;
    --card: #000000;
    --band: #027067;
    --accent: #0b7f74;
    --accent-bright: #11867a;
    --text: #f2f2f2;
    --text-soft: #d9d9d9;
  }
  * { box-sizing: border-box; margin: 0; padding: 0; }
  html, body { width: 1200px; height: 900px; overflow: hidden; }
  body {
    position: relative;
    background: var(--backdrop);
    font-family: "Exo 2", sans-serif;
    color: var(--text);
  }
  .card {
    position: absolute;
    background: var(--card);
  }
  .card__band {
    position: absolute;
    left: 0; right: 0; bottom: 0;
    height: 13px;
    background: var(--band);
  }
  .card--front { left: 300px; top: 77px; width: 602px; height: 343px; }
  .card--back  { left: 297px; top: 479px; width: 606px; height: 346px; }

  .brand { position: absolute; display: flex; flex-direction: column; align-items: center; }
  .brand__row { display: flex; align-items: center; }
  .brand__mark { background: var(--accent); flex: none; }
  .brand__name {
    font-weight: 500;
    color: var(--text);
    text-transform: uppercase;
    line-height: 1.05;
  }
  .brand__tagline { font-weight: 500; color: var(--text); white-space: nowrap; }

  .card--front .brand { left: 0; right: 0; top: 120px; }
  .card--front .brand__mark { width: 62px; height: 62px; margin-right: 18px; }
  .card--front .brand__name { font-size: 30px; letter-spacing: 1px; }
  .card--front .brand__tagline { font-size: 21px; margin-top: 14px; letter-spacing: .3px; }

  .card--back .brand { left: 40px; width: 250px; top: 138px; }
  .card--back .brand__mark { width: 46px; height: 46px; margin-right: 12px; }
  .card--back .brand__name { font-size: 21px; letter-spacing: .6px; }
  .card--back .brand__tagline { font-size: 14px; margin-top: 12px; letter-spacing: .3px; }

  .divider {
    position: absolute;
    left: 302px; top: 72px;
    width: 3px; height: 196px;
    background: var(--accent);
  }
  .contact { position: absolute; left: 338px; top: 66px; width: 260px; }
  .contact__name { font-size: 23px; font-weight: 500; color: var(--accent-bright); letter-spacing: .5px; }
  .contact__role { font-size: 12px; color: var(--text-soft); margin-top: 2px; }
  .contact__address { font-size: 13px; color: var(--accent); margin-top: 11px; line-height: 16px; }
  .contact__list { list-style: none; margin-top: 16px; }
  .contact__item {
    display: flex; align-items: center;
    height: 26.5px;
    font-size: 14px; color: var(--text-soft); letter-spacing: .3px;
  }
  .contact__icon { width: 20px; height: 20px; margin-right: 14px; fill: var(--accent); flex: none; }
</style>
</head>
<body>

  <section class="card card--front" aria-label="Card front">
    <div class="brand">
      <div class="brand__row">
        <span class="brand__mark" aria-hidden="true"></span>
        <span class="brand__name">Holvaster<br>Building Inc.</span>
      </div>
      <p class="brand__tagline">Professional . Quality . Service</p>
    </div>
    <div class="card__band"></div>
  </section>

  <section class="card card--back" aria-label="Card back">
    <div class="brand">
      <div class="brand__row">
        <span class="brand__mark" aria-hidden="true"></span>
        <span class="brand__name">Holvaster<br>Building Inc.</span>
      </div>
      <p class="brand__tagline">Professional . Quality . Service</p>
    </div>

    <div class="divider"></div>

    <div class="contact">
      <h1 class="contact__name">Marcus Ellery</h1>
      <p class="contact__role">CEO | Founder</p>
      <p class="contact__address">18 North Tamlin Glen Road, Unit 57,<br>Marbrook Vale, ON, K7T 2R9</p>
      <ul class="contact__list">
        <li class="contact__item">
          <svg class="contact__icon" viewBox="0 0 24 24" aria-hidden="true"><path d="M6.6 10.8a15.1 15.1 0 0 0 6.6 6.6l2.2-2.2c.3-.3.7-.4 1-.2 1.1.4 2.3.6 3.6.6.6 0 1 .4 1 1V20c0 .6-.4 1-1 1A17 17 0 0 1 3 4c0-.6.4-1 1-1h3.5c.6 0 1 .4 1 1 0 1.3.2 2.5.6 3.6.1.3 0 .7-.2 1z"/></svg>
          905-218-5937
        </li>
        <li class="contact__item">
          <svg class="contact__icon" viewBox="0 0 24 24" aria-hidden="true"><path d="M7 1h10a2 2 0 0 1 2 2v18a2 2 0 0 1-2 2H7a2 2 0 0 1-2-2V3a2 2 0 0 1 2-2zm1 3v7h8V4zm0 9v2h2v-2zm3 0v2h2v-2zm3 0v2h2v-2zm-6 3v2h2v-2zm3 0v2h2v-2zm3 0v2h2v-2z"/></svg>
          905-218-5937
        </li>
        <li class="contact__item">
          <svg class="contact__icon" viewBox="0 0 24 24" aria-hidden="true"><path d="M2 5h20v14H2zm2 2v.4l8 5.2 8-5.2V7zm0 2.8V17h16V9.8l-8 5.2z"/></svg>
          ellery@holvaster-example.com
        </li>
        <li class="contact__item">
          <svg class="contact__icon" viewBox="0 0 24 24" aria-hidden="true"><path d="M12 2a10 10 0 1 0 0 20 10 10 0 0 0 0-20zm6.9 6h-3a15 15 0 0 0-1.3-3.6A8 8 0 0 1 18.9 8zM12 4c.8 1.2 1.5 2.5 1.9 4h-3.8c.4-1.5 1.1-2.8 1.9-4zM4.3 14a8 8 0 0 1 0-4h3.4a16 16 0 0 0 0 4zm.8 2h3a15 15 0 0 0 1.3 3.6A8 8 0 0 1 5.1 16zm3-8h-3a8 8 0 0 1 4.3-3.6C8.8 5.6 8.4 6.8 8.1 8zM12 20c-.8-1.2-1.5-2.5-1.9-4h3.8c-.4 1.5-1.1 2.8-1.9 4zm2.3-6H9.7a14 14 0 0 1 0-4h4.6a14 14 0 0 1 0 4zm.3 5.6c.6-1.1 1-2.3 1.3-3.6h3a8 8 0 0 1-4.3 3.6zm1.7-5.6a16 16 0 0 0 0-4h3.4a8 8 0 0 1 0 4z"/></svg>
          www.holvaster-example.com
        </li>
      </ul>
    </div>

    <div class="card__band"></div>
  </section>

</body>
</html>
```